VANDREL 2020

I have a front picture for the CD; I have all of the info for the back cover; I need someone to put my idea together with the correct specs; I require a very FAST TURN AROUND!!! I need to get this project to the CD replicator by next week ASAP...

```html
<!DOCTYPE html>
<html lang="en">
<head>
<meta charset="utf-8">
<title>VANDREL 2020 – CD Cover</title>
<link href="https://fonts.googleapis.com/css2?family=Poppins:wght@400;700;800;900&family=Abril+Fatface&display=swap" rel="stylesheet">
<style>
  :root{
    --backdrop:#4f4f4f;
    --navy:#1c2f56;
    --navy-deep:#0f2148;
    --navy-mid:#2c4577;
    --silver-light:#f2f2f2;
    --silver-dark:#a9a9a9;
    --red:#c8161d;
    --red-dark:#9e0f14;
    --flag-red:#d7262c;
    --flag-blue:#2a4a9c;
    --white:#ffffff;
    --ink:#ffffff;
  }
  *{box-sizing:border-box;margin:0;padding:0}
  html,body{width:1200px;height:641px;overflow:hidden;background:var(--backdrop)}
  .canvas{position:relative;width:1200px;height:641px}

  /* Front cover */
  .front-cover{position:absolute;left:68px;top:69px;width:510px;height:489px;overflow:hidden;background:var(--red)}
  .front-header{position:absolute;left:0;top:0;width:510px;height:150px;
    background:radial-gradient(ellipse at 50% 100%,#5e78ad 0%,var(--navy-mid) 35%,var(--navy) 75%)}
  .front-title{position:absolute;left:0;top:12px;width:100%;text-align:center;
    font-family:"Poppins",sans-serif;font-weight:900;font-size:78px;line-height:1;color:#f1f1f1;
    letter-spacing:-1px;text-shadow:0 3px 4px rgba(0,0,0,.45)}
  .front-tagline{position:absolute;left:0;top:112px;width:100%;text-align:center;
    font-family:"Poppins",sans-serif;font-weight:700;font-size:17px;letter-spacing:5px;color:var(--ink)}
  .silver-strip{position:absolute;left:0;top:150px;width:510px;height:14px;
    background:linear-gradient(var(--silver-light),var(--silver-dark))}
  .front-photo{position:absolute;left:0;top:164px;width:510px;height:250px;
    background:linear-gradient(90deg,var(--flag-blue) 0%,#6a6fa8 30%,#e9e3e3 50%,var(--flag-red) 75%,#efe4e4 100%)}
  .front-frame{position:absolute;left:0;top:396px;width:510px;height:30px}
  .front-artist{position:absolute;left:0;top:431px;width:100%;text-align:center;
    font-family:"Abril Fatface",serif;font-size:31px;letter-spacing:2px;color:#f4eaea;
    text-shadow:0 2px 3px rgba(0,0,0,.35)}
  .front-base{position:absolute;left:0;top:412px;width:510px;height:77px;
    background:linear-gradient(var(--red),var(--red-dark))}

  /* Back cover */
  .back-cover{position:absolute;left:690px;top:65px;width:494px;height:493px;overflow:hidden;background:var(--navy-deep)}
  .back-header{position:absolute;left:0;top:0;width:494px;height:89px;background:var(--navy-deep)}
  .back-title{position:absolute;left:0;top:10px;width:100%;text-align:center;
    font-family:"Poppins",sans-serif;font-weight:800;font-size:43px;line-height:1;color:var(--white);letter-spacing:-1px}
  .back-artist{position:absolute;left:0;top:60px;width:100%;text-align:center;
    font-family:"Abril Fatface",serif;font-size:17px;letter-spacing:1.5px;color:var(--white)}
  .back-collage{position:absolute;left:130px;top:89px;width:364px;height:404px;
    background:
      linear-gradient(90deg,var(--navy-deep) 0%,rgba(15,33,72,0) 40%),
      linear-gradient(180deg,#b54a55 0%,#6d5f86 36%,#2f4fa2 50%,#c9ccdc 66%,#8e5b63 80%,#c98f86 100%)}
  .track-list{position:absolute;left:26px;top:104px;list-style:none;
    font-family:"Poppins",sans-serif;font-weight:700;font-size:12.5px;color:var(--white);
    text-shadow:0 1px 3px rgba(0,0,0,.7)}
  .track-list li{height:32.8px;line-height:18px;letter-spacing:-.2px}
  .label-box{position:absolute;left:21px;top:404px;width:53px;height:25px;background:var(--white)}
  .legal-text{position:absolute;left:21px;top:437px;width:285px;
    font-family:"Poppins",sans-serif;font-weight:400;font-size:7.4px;line-height:8.6px;color:var(--white)}
</style>
</head>
<body>
<div class="canvas">

  <section class="front-cover">
    <div class="front-header">
      <h1 class="front-title">VANDREL</h1>
      <p class="front-tagline">MUSIC THAT RINGS TRUTH</p>
    </div>
    <div class="silver-strip"></div>
    <div class="front-photo" role="img" aria-label="Photo of the candidate with open arms before an American flag and large 2020 numerals"></div>
    <div class="front-base"></div>
    <svg class="front-frame" viewBox="0 0 510 30" aria-hidden="true">
      <defs>
        <linearGradient id="silver" x1="0" y1="0" x2="0" y2="1">
          <stop offset="0" stop-color="#f4f4f4"/>
          <stop offset="1" stop-color="#9c9c9c"/>
        </linearGradient>
      </defs>
      <polygon points="0,4 130,4 148,16 362,16 380,4 510,4 510,16 384,16 366,28 144,28 126,16 0,16" fill="url(#silver)"/>
    </svg>
    <p class="front-artist">Leo Marcelli</p>
  </section>

  <section class="back-cover">
    <div class="back-header">
      <h2 class="back-title">VANDREL 2020</h2>
      <p class="back-artist">Leo Marcelli</p>
    </div>
    <div class="back-collage" role="img" aria-label="Collage of rally photos with supporters, campaign signs and the candidate speaking"></div>
    <ol class="track-list">
      <li>1. VANDREL DERANGEMENT SYNDROME</li>
      <li>2. WOW THING</li>
      <li>3. STAR SPANGLED BANNER</li>
      <li>4. AMERICA IS BEAUTIFUL</li>
      <li>5. LET VANDREL BE VANDREL</li>
      <li>6. I BELIEVE IN HIM</li>
      <li>7. HE’S SO BAD</li>
      <li>8. NEVER VANDREL BLUES</li>
      <li>9. VISTA DEL SOL</li>
    </ol>
    <div class="label-box"></div>
    <p class="legal-text">Lorem ipsum dolor sit amet, consectetur adipiscing elit, sed do eiusmod tempor incididunt ut labore et dolore magna aliqua. Ut enim ad minim veniam, quis nostrud exercitation ullamco laboris nisi ut aliquip ex ea commodo consequat.</p>
  </section>

</div>
</body>
</html>
```